Tattoo Shop Business Card

I need a Business Card for the The Harbor Quill.

I'm thinking i want a double sided business card, really clean, very classy, one side the logo, and on the other my information. I'm pretty much open to anything, as long as its fun and captures class and elegance, while at the same time is edgy and tattooish.
I don't want your typical classic card. Add your own twist on it

Logo is attached to this brief

Please include:
Name
Position
Phone Number
Email
Website

Target Market(s)

I'm looking to capture potential clients for my tattoo shop so the card needs to be something they can fit in their wallet but they will also remember me when they see that card in there. My target audience is everyone over 18 that is intrigued by tattoos and piercings.

Industry/Entity Type

Business

Font styles to use
Serif

Colors

Designer to choose colors to be used in the design.

Requirements
Must have
• must be bold and something people will never forget

```html
<!DOCTYPE html>
<html lang="en">
<head>
<meta charset="utf-8">
<title>The Harbor Quill — Business Card</title>
<link rel="stylesheet" href="https://fonts.googleapis.com/css2?family=Lato:wght@300;400;700;900&display=swap">
<style>
  :root {
    --backdrop: #c8c8c9;
    --card-light: #ececec;
    --card-mid: #d9d9d9;
    --ink: #111111;
    --ink-soft: #3a3a3a;
    --paper: #ffffff;
    --band: #cfcfcf;
  }
  * { margin: 0; padding: 0; box-sizing: border-box; }
  html, body { width: 1200px; height: 800px; overflow: hidden; }
  body {
    background: var(--backdrop);
    font-family: "Lato", Arial, sans-serif;
    color: var(--ink);
    position: relative;
  }
  .card {
    position: absolute;
    top: 245px;
    width: 520px;
    height: 300px;
    overflow: hidden;
    background: linear-gradient(160deg, var(--paper) 0%, var(--card-light) 45%, var(--card-mid) 100%);
    box-shadow: 0 6px 18px rgba(0,0,0,0.18);
  }
  .card--info { left: 60px; }
  .card--logo { left: 620px; }

  /* Info side */
  .info-dark {
    position: absolute;
    inset: 0;
    background: var(--ink);
    clip-path: polygon(0 112px, 100% 192px, 100% 100%, 0 100%);
  }
  .info-name {
    position: absolute; left: 30px; top: 26px;
    font-size: 17px; font-weight: 700; letter-spacing: 1.5px;
  }
  .info-role {
    position: absolute; left: 31px; top: 47px;
    font-size: 8px; font-weight: 400; letter-spacing: 1.5px; color: var(--ink-soft);
    text-transform: uppercase;
  }
  .info-quote {
    position: absolute; left: 30px; top: 72px;
    font-size: 9px; font-weight: 400; letter-spacing: 1.5px; color: var(--ink-soft);
  }
  .services {
    position: absolute; right: 28px; top: 52px;
    list-style: none; text-align: right;
    font-size: 8px; letter-spacing: 1.2px; color: var(--ink-soft); text-transform: uppercase;
  }
  .services li { margin-bottom: 9px; }
  .services li::after { content: " \2022"; color: var(--ink); }
  .info-mark {
    position: absolute; left: 30px; top: 150px;
    display: flex; align-items: center; gap: 8px;
    font-size: 18px; font-weight: 900; letter-spacing: 1px;
    color: var(--paper); text-transform: uppercase;
  }
  .info-mark .dot {
    width: 9px; height: 9px; border-radius: 50%; background: var(--paper);
  }
  .contact {
    position: absolute; right: 28px; bottom: 16px;
    list-style: none; color: var(--paper);
    font-size: 9px; letter-spacing: 1.2px; text-transform: uppercase;
  }
  .contact li {
    display: flex; align-items: center; justify-content: flex-end; gap: 10px;
    margin-top: 8px;
  }
  .contact svg { width: 20px; height: 20px; flex: none; }

  /* Logo side */
  .logo-mark {
    position: absolute; left: 0; right: 0; top: 92px;
    display: flex; align-items: center; justify-content: center; gap: 14px;
    font-size: 40px; font-weight: 900; letter-spacing: 2px;
    color: var(--ink); text-transform: uppercase;
  }
  .logo-mark .dot {
    width: 16px; height: 16px; border-radius: 50%; background: var(--ink);
  }
  .logo-tag {
    position: absolute; left: 0; right: 0; top: 150px; text-align: center;
    font-size: 10px; font-weight: 700; letter-spacing: 4px; color: var(--ink-soft);
    text-transform: uppercase;
  }
  .logo-band {
    position: absolute; left: 0; right: 0; bottom: 42px; height: 30px;
    background: linear-gradient(90deg, rgba(0,0,0,0) 0%, var(--band) 30%, var(--band) 70%, rgba(0,0,0,0) 100%);
    display: flex; align-items: center; justify-content: center;
    font-size: 9px; letter-spacing: 3px; color: var(--ink-soft); text-transform: uppercase;
  }
</style>
</head>
<body>

  <section class="card card--info" aria-label="Business card, contact side">
    <div class="info-dark"></div>
    <h1 class="info-name">THE HARBOR QUILL</h1>
    <p class="info-role">Tattoo Designer</p>
    <p class="info-quote">" MY WORK SPEAKS FOR ITSELF "</p>
    <ul class="services">
      <li>Custom Tattoo</li>
      <li>Body Piercing</li>
      <li>Tattoo After Care</li>
      <li>Free Test Temporary Tattoo</li>
    </ul>
    <div class="info-mark"><span class="dot"></span>The Harbor Quill</div>
    <ul class="contact">
      <li>000 . 1234 . 5678
        <svg viewBox="0 0 20 20"><circle cx="10" cy="10" r="9" fill="none" stroke="#fff" stroke-dasharray="2 1.5"/><path d="M7 6l2 0 1 2.5-1.2 1a5 5 0 0 0 2.7 2.7l1-1.2 2.5 1 0 2c-4 .5-8.5-4-8-8z" fill="#fff"/></svg>
      </li>
      <li>theharborquill@mail.com
        <svg viewBox="0 0 20 20"><circle cx="10" cy="10" r="9" fill="none" stroke="#fff" stroke-dasharray="2 1.5"/><rect x="5.5" y="7" width="9" height="6.5" fill="#fff"/><path d="M5.5 7l4.5 3.5L14.5 7" fill="none" stroke="#111" stroke-width=".8"/></svg>
      </li>
      <li>www.theharborquill.com
        <svg viewBox="0 0 20 20"><circle cx="10" cy="10" r="9" fill="none" stroke="#fff" stroke-dasharray="2 1.5"/><circle cx="10" cy="10" r="4.5" fill="none" stroke="#fff"/><ellipse cx="10" cy="10" rx="2" ry="4.5" fill="none" stroke="#fff" stroke-width=".8"/><path d="M5.5 10h9" stroke="#fff" stroke-width=".8"/></svg>
      </li>
    </ul>
  </section>

  <section class="card card--logo" aria-label="Business card, logo side">
    <div class="logo-mark"><span class="dot"></span>The Harbor Quill</div>
    <p class="logo-tag">Fine Tattoos · Bayside · And Piercing</p>
    <div class="logo-band">www.theharborquill.com</div>
  </section>

</body>
</html>
```